Dunmore Partners Brochure Design

Design a brochure for Dunmore Partners, with a focus on the three key areas of the business:
- Business Advisory (consulting);
- Turnaround;
- Business Valuations.

Details in relation to the above available at www.dunmorepartners-example.com

The aim of the document is to have something which works in a digital and physical form. The brochure should have each of the above areas on a separate A4 page so as to enable them to be presented digitally as stand alone brochures. Alternative designs which achieve the same will be accepted, I.e. Multiple brochures, one for whole of business and one for each business area.

Should also have a brief bio on Colin Brady and Dunmore Partners, also on a separate page or included in separate brochures if this approach is taken.

Industry/Entity Type

Digital

Requirements
Must have
• Please ensure that design flows from website.

```html
<!DOCTYPE html>
<html lang="en">
<head>
<meta charset="utf-8">
<title>Dunmore Partners – About Us &amp; Executive Team</title>
<link href="https://fonts.googleapis.com/css2?family=Advent+Pro:wght@300;400;500&family=Play:wght@400;700&family=Michroma&display=swap" rel="stylesheet">
<style>
  :root{
    --blue-deep:#164c8f;
    --blue-mid:#1d6fb4;
    --blue-light:#2a8ccc;
    --blue-text:#1b4f96;
    --link-blue:#3a6fb0;
    --heading-blue:#1a3f8a;
    --gold:#f5c518;
    --intro-text:#d6e6f7;
    --body-text:#555b61;
    --list-text:#333;
    --orange-a:#f9a51d;
    --orange-b:#f58a0a;
    --footer-text:#6b3a05;
    --page:#ffffff;
  }
  *{margin:0;padding:0;box-sizing:border-box}
  html,body{width:1200px;height:800px;overflow:hidden;background:var(--page)}
  .page{position:relative;width:1200px;height:800px;overflow:hidden;
    background:linear-gradient(180deg,#fff 0%,#f1f3f5 45%,#fafbfc 80%,#fff 100%);
    font-family:"Play",sans-serif;color:var(--body-text)}

  /* About Us header panel */
  .about-banner{position:absolute;left:0;top:0;width:603px;height:290px;
    background:linear-gradient(125deg,#0f3f80 0%,#1a5ea6 45%,#2a7fc2 70%,#174f93 100%)}
  .about-banner__pointer{position:absolute;left:535px;top:290px}
  .about-title{position:absolute;right:638px;top:132px;font-family:"Advent Pro",sans-serif;
    font-weight:300;font-size:42px;letter-spacing:3px;color:#fff;text-align:right;line-height:1}
  .about-rule{position:absolute;left:0;top:172px;width:561px;height:1px;background:#fff}
  .about-intro{position:absolute;left:14px;top:203px;width:549px;text-align:right;
    font-size:17px;line-height:25px;color:var(--intro-text);font-weight:400}
  .brand{color:var(--gold);font-size:19px}

  .about-body{position:absolute;left:43px;top:316px;width:526px;font-size:13.5px;
    line-height:20.4px;text-align:justify}
  .about-body p{margin-bottom:20px}
  .about-body p.tight{margin-bottom:0}
  .about-body p.values-intro{margin-top:20px}
  .name-link{color:var(--link-blue);font-size:16px}
  .values{list-style:none;margin-top:-2px}
  .values li{position:relative;padding-left:20px;margin-bottom:13px}
  .chevron{position:absolute;left:3px;top:6px}
  .values .chevron{left:2px}

  /* Executive Team header band */
  .exec-banner{position:absolute;left:603px;top:0;width:597px;height:111px;
    background:linear-gradient(100deg,#1b73b8 0%,#1f6aae 50%,#143f86 100%)}
  .exec-banner__pointer{position:absolute;left:1143px;top:111px}
  .exec-rule{position:absolute;left:603px;top:71px;width:567px;height:1px;background:#fff}
  .exec-title{position:absolute;right:32px;top:36px;font-family:"Advent Pro",sans-serif;
    font-weight:400;font-size:40px;letter-spacing:2px;color:#fff;line-height:1}

  .profile-lead{position:absolute;left:642px;top:136px;width:531px;font-size:18px;
    line-height:26px;color:#4a4f55;text-align:justify}
  .profile-lead .name-link{font-size:19px;color:var(--blue-text)}
  .portrait{position:absolute;left:642px;top:205px;width:168px;height:194px;
    border:3px solid var(--blue-light);
    background:linear-gradient(160deg,#3a3330 0%,#1d1a19 60%,#2c2a2b 100%)}
  .profile-bio{position:absolute;left:825px;top:199px;width:348px;font-size:13.5px;
    line-height:23.2px;text-align:justify}
  .profile-bio p{margin-bottom:23px}

  .qual-title{position:absolute;left:825px;top:453px;font-size:18px;font-weight:400;color:var(--heading-blue)}
  .qual-list{position:absolute;left:840px;top:486px;list-style:none;font-size:13.5px;
    line-height:23.2px;color:var(--list-text)}
  .qual-list li{position:relative;padding-left:18px}
  .qual-list .chevron{left:0;top:7px}
  .contact{position:absolute;left:825px;font-size:16px;color:var(--heading-blue)}
  .contact--phone{top:601px}
  .contact--email{top:648px}

  .footer{position:absolute;left:0;top:756px;width:1200px;height:44px;
    background:linear-gradient(90deg,var(--orange-a) 0%,var(--orange-b) 50%,var(--orange-a) 100%)}
  .footer__url{position:absolute;top:16px;font-family:"Michroma",sans-serif;font-size:11px;
    letter-spacing:1.5px;color:var(--footer-text);text-transform:uppercase}
  .footer__url--left{left:16px}
  .footer__url--right{right:16px}
</style>
</head>
<body>
<div class="page">

  <div class="about-banner" role="img" aria-label="Blue-toned business handshake photograph"></div>
  <svg class="about-banner__pointer" width="26" height="13" viewBox="0 0 26 13"><path d="M0 0H26L13 13Z" fill="#1a5ea6"/></svg>
  <div class="about-rule"></div>
  <h1 class="about-title">About Us</h1>
  <p class="about-intro"><span class="brand">Dunmore Partners</span> have identified that the traditional business advisory services being offered to small and medium sized business do not adequately meet the needs of these businesses.</p>

  <div class="about-body">
    <p>Traditional service providers to this sector do not provide the information or skills needed to drive these businesses.</p>
    <p class="tight"><span class="name-link">Dunmore Partners</span> focuses on the implementation of efficient process and effective technology to businesses to proactively manage information and allow us to provide timely professional advice. We understand that small to medium businesses are cost sensitive and value is a key driver in any decision. With this in mind we aim to build a relationship based upon trust, which the business relies upon for advice and believes plays a valuable role driving their businesses.<br>Values</p>
    <p class="values-intro"><span class="name-link">Dunmore Partners</span> has three key values, which we see underpinning our business and our offering to clients:</p>
    <ul class="values">
      <li><svg class="chevron" width="8" height="10" viewBox="0 0 8 10"><path d="M1 1L6 5L1 9" fill="none" stroke="#1a5ea6" stroke-width="2.4"/></svg>An understanding of the importance of earning the trust of management;</li>
      <li><svg class="chevron" width="8" height="10" viewBox="0 0 8 10"><path d="M1 1L6 5L1 9" fill="none" stroke="#1a5ea6" stroke-width="2.4"/></svg>A focus on driving value for client, ensuring that clients see value in our offering;</li>
      <li><svg class="chevron" width="8" height="10" viewBox="0 0 8 10"><path d="M1 1L6 5L1 9" fill="none" stroke="#1a5ea6" stroke-width="2.4"/></svg>Using technology to drive efficiencies in our practice and our clients businesses.</li>
    </ul>
  </div>

  <div class="exec-banner" role="img" aria-label="Blue-toned photograph of business people silhouettes"></div>
  <svg class="exec-banner__pointer" width="26" height="13" viewBox="0 0 26 13"><path d="M0 0H26L13 13Z" fill="#143f86"/></svg>
  <div class="exec-rule"></div>
  <h2 class="exec-title">Executive Team</h2>

  <p class="profile-lead"><span class="name-link">Colin Brady</span> With experience in Tax, Audit and Insolvency in both big 4 and mid-tier firms</p>
  <div class="portrait" role="img" aria-label="Portrait photograph of Colin Brady"></div>
  <div class="profile-bio">
    <p>With experience in Tax, Audit and Insolvency in both big 4 and mid-tier firms, Colin has thrived working with businesses to solve their problems and assist them to grow.</p>
    <p>However, through this work, Colin identified that SME businesses were not provided the service they deserved. In launching Dunmore Partners, Colin’s aim is to provide businesses with a professional advisor who they can trust to give both timely and accurate advice.</p>
  </div>

  <h3 class="qual-title">Qualifications:</h3>
  <ul class="qual-list">
    <li><svg class="chevron" width="8" height="10" viewBox="0 0 8 10"><path d="M1 1L6 5L1 9" fill="none" stroke="#1a5ea6" stroke-width="2.4"/></svg>Chartered Accountant</li>
    <li><svg class="chevron" width="8" height="10" viewBox="0 0 8 10"><path d="M1 1L6 5L1 9" fill="none" stroke="#1a5ea6" stroke-width="2.4"/></svg>Masters of Business Law</li>
    <li><svg class="chevron" width="8" height="10" viewBox="0 0 8 10"><path d="M1 1L6 5L1 9" fill="none" stroke="#1a5ea6" stroke-width="2.4"/></svg>Bachelor of Business (accounting)</li>
    <li><svg class="chevron" width="8" height="10" viewBox="0 0 8 10"><path d="M1 1L6 5L1 9" fill="none" stroke="#1a5ea6" stroke-width="2.4"/></svg>Bachelor of Information Systems</li>
  </ul>
  <p class="contact contact--phone">Phone : 0400 555 017</p>
  <p class="contact contact--email">Email: colinbrady@dunmorepartners-example.com</p>

  <footer class="footer">
    <span class="footer__url footer__url--left">www.dunmorepartners-example.com</span>
    <span class="footer__url footer__url--right">www.dunmorepartners-example.com</span>
  </footer>
</div>
</body>
</html>
```